Website for peer to peer car sharing service

Hi all,

We need a web design for a new environmental friendly peer-to-peer car sharing website.

The website will serve as a marketplace where car owners can list their car and drivers that who do not have access to a car can rent a suitable car. It is important for us to emphasis that this is a community where the main purpose is to use the vehicles on the street in a more efficient way.

Attached are five pictures where we have sketched up the five main pages:

File 1. Info site for a particular car.
File 2. Logo.
File 3. Register a car.
File 4. Sign up.
File 5. Search.
File 6. Front page.

The logo for the company is attached (File 2) and it would be ideal to design the website in relation to the logo. The final design should relate to a secure market place which is environmental friendly.

We would like this webpage to be in the same spirit as www.velnoro.it, www.brundale.com, www.plimtrovesite.com, https://wend.kul.net, https://garbelow.com etc.

We look forward to see your designs.

Best regards,
The Trundo Team.

Hi guys, 

Please take :

1) Could you please design icons for for  'FAQ' and 'Insurance' in the header, locate the icons right to the Trundo logo. We only want two icons ('FAQ' and 'Insurance')  right to the Trundo logo.

2) The height of the header should be the same as the header of faplex.com

3) The price tags for the cars (below the top section) should be similar to the price tags at mostanbee.com.

4) We would like you to start to design the other pages (the sub-pages listed in the project description:
a)Info site for a particular car.
b)Register a car. 
c)Search results (similar to http://www.pevrotank.com/find-car).

Please take a look at the picture attached for the sub-pages:

https://files.quenmolt.example/brief_uploads/000001_3_search_000001_brief000001.jpg

https://files.quenmolt.example/brief_uploads/000002_4_infositeforaparticularcar_000002_brief000002.jpg

http://www.quenmolt.example/file.aspx?fileLocation=storage_url/brief_uploads/000003_5_registeracar_brief000003.jpg

Best regards, 
Trundo team 

Target Market(s)

The target market are people from 20-40 years old who are environmental friendly, also tourists who visit the city and would like to rent a car.

Industry/Entity Type

It Company

Requirements
Must have
• It is required that the designer that will be chosen will hand in layered PSD files of each web page.

```html
<!DOCTYPE html>
<html lang="en">
<head>
<meta charset="utf-8">
<title>Trundo – Peer to peer car sharing</title>
<link href="https://fonts.googleapis.com/css2?family=Oswald:wght@400;600&family=Open+Sans:wght@400;600;700&display=swap" rel="stylesheet">
<style>
:root{
  --green:#8cc63f;
  --green-dark:#6fa52a;
  --ink:#2b2b2b;
  --text:#555;
  --muted:#888;
  --band:#dfe0e3;
  --white:#fff;
  --footer:#1f1f1f;
  --footer-top:#2e2e2e;
  --line:#c9cacd;
}
*{margin:0;padding:0;box-sizing:border-box}
html,body{width:717px;height:1200px;overflow:hidden}
body{font-family:"Open Sans",Arial,sans-serif;color:var(--text);background:var(--white);position:relative;font-size:8px;line-height:1.45}
.heading{font-family:"Oswald","Arial Narrow",sans-serif;font-weight:600;text-transform:uppercase;color:var(--ink);letter-spacing:.3px}
.green{color:var(--green)}
.read-more{display:inline-block;margin-top:6px;font-weight:700;color:var(--ink);font-size:8px}

/* header + hero */
.hero{position:absolute;left:0;top:0;width:717px;height:335px;background:linear-gradient(115deg,#c7a98c 0%,#a88468 22%,#7b5d4d 40%,#a72a33 55%,#5c1f24 70%,#3d3b3f 100%)}
.topbar{position:absolute;left:0;top:0;width:717px;height:28px;background:rgba(20,20,20,.85);display:flex;align-items:center;justify-content:space-between;padding:0 14px 0 92px}
.brand{position:absolute;left:16px;top:6px;display:flex;align-items:center;gap:5px;font-family:"Open Sans",sans-serif;font-weight:700;font-size:17px;color:var(--white)}
.brand-dot{width:11px;height:11px;border-radius:50%;background:var(--green)}
.top-links{margin-left:auto;display:flex;gap:14px;font-size:8px;color:#ddd}
.top-links span::before{content:"";display:inline-block;width:7px;height:7px;border-radius:50%;background:var(--green);margin-right:4px;vertical-align:-1px}
.hero-title{position:absolute;left:425px;top:216px;font-family:"Oswald",sans-serif;font-weight:600;font-size:20px;color:var(--white);letter-spacing:.4px}
.hero-sub{position:absolute;left:425px;top:244px;width:270px;color:#eee;font-size:7.5px}
.search{position:absolute;left:200px;top:290px;display:flex;height:30px}
.search-input{width:270px;background:rgba(255,255,255,.92);border:1px solid #ccc;padding:7px 10px;color:#999;font-size:10px}
.search-btn{width:95px;background:var(--green);color:var(--ink);font-weight:600;font-size:10px;display:flex;align-items:center;justify-content:center}

/* car cards */
.cars{position:absolute;left:88px;top:352px;width:541px;display:flex;gap:14px}
.car{width:171px;background:var(--white);border:1px solid #ddd;box-shadow:0 1px 3px rgba(0,0,0,.15)}
.car-photo{position:relative;height:88px;background:linear-gradient(180deg,#f3f3f3,#cfd2d6)}
.price-tag{position:absolute;left:6px;top:0;width:36px;height:32px;background:var(--green);color:var(--white);font-family:"Oswald",sans-serif;font-size:10px;line-height:1.05;text-align:center;padding-top:4px}
.price-tag small{display:block;font-size:8px}
.owner{display:flex;gap:5px;padding:5px;background:#f2f2f2;border-top:1px solid #e4e4e4}
.owner-photo{width:28px;height:28px;background:linear-gradient(135deg,#c9b3a0,#7d6a5e)}
.owner-name{font-weight:700;color:var(--ink);font-size:7.5px}
.owner-note{font-size:7px;color:var(--muted)}
.owner-note::before{content:"";display:inline-block;width:6px;height:6px;background:var(--green);margin-right:3px}

/* feature bands */
.band{position:absolute;left:0;width:717px}
.band-grey{background:var(--band);border-top:3px solid #c4c6ca}
.inner{position:absolute;left:88px;width:541px}
.feature-one{top:508px;height:140px}
.feature-two{top:660px;height:150px;background:var(--white)}
.feature-three{top:822px;height:138px}
.feature-text p{margin-top:6px}
.video{position:absolute;right:0;top:14px;width:176px;height:104px;background:linear-gradient(120deg,#9fb3c4,#546373 60%,#2f3640);display:flex;align-items:center;justify-content:center}
.play{width:28px;height:28px;border-radius:50%;background:rgba(255,255,255,.85);display:flex;align-items:center;justify-content:center}
.hand-car{position:absolute;left:0;top:12px;width:160px;height:116px;background:radial-gradient(ellipse at 50% 55%,#d93a32 0%,#d9a98e 38%,#f1ece8 70%)}
.widget{position:absolute;right:0;top:12px;width:176px;height:114px;background:var(--white);border:1px solid var(--line)}
.widget-head{height:22px;background:#6b6e73;color:var(--white);display:flex;align-items:center;justify-content:space-between;padding:0 8px;font-weight:700;font-size:9px}
.widget-body{padding:6px 8px;font-size:7px}
.fans{display:flex;gap:4px;margin-top:6px}
.fan{width:22px;height:22px;background:linear-gradient(135deg,#b8bcc2,#7d828a)}
.widget-btn{position:absolute;right:8px;bottom:8px;background:#e9eaee;border:1px solid #ccc;padding:1px 8px;font-size:7px}

/* press */
.press{position:absolute;left:88px;top:972px;width:541px}
.press-title{font-size:17px}
.press-row{margin-top:12px;display:flex;align-items:center;justify-content:space-between;border-top:1px solid #e4e4e4;border-bottom:1px solid #e4e4e4;height:50px;padding:0 6px}
.press-name{font-family:"Oswald",sans-serif;font-weight:600;font-size:14px;color:var(--ink)}
.arrow{font-size:18px;color:#666;font-weight:700}

/* footer */
.footer{position:absolute;left:0;top:1088px;width:717px;height:112px;background:var(--footer);color:#bbb}
.footer-heads{height:18px;background:var(--footer-top);display:flex;padding-left:88px}
.footer-heads span{width:135px;color:var(--white);font-weight:700;font-size:8.5px;line-height:18px}
.footer-cols{display:flex;padding:6px 0 0 88px}
.fcol{width:135px;font-size:7px;line-height:1.6}
.fcol li{list-style:none}
.fcol li::before{content:"› ";color:var(--green)}
.contact-line{display:flex;align-items:center;gap:4px}
.contact-line i{display:inline-block;width:7px;height:7px;background:var(--green);border-radius:50%}
.world{width:110px;height:58px;background:linear-gradient(180deg,#3a3a3a,#2a2a2a)}
.socials{display:flex;gap:4px}
.socials i{width:13px;height:13px;border-radius:50%;background:#555;display:block}
.foot-brand{display:flex;align-items:center;gap:5px;margin-top:8px;font-weight:700;font-size:16px;color:var(--white)}
.copy{font-size:6.5px;color:#888;margin-top:3px}
</style>
</head>
<body>

<section class="hero" role="img" aria-label="Photo of smiling young friends standing beside a red car">
  <header class="topbar">
    <nav class="top-links"><span>List your car</span><span>Login</span><span>Signup</span></nav>
  </header>
  <div class="brand"><span class="brand-dot"></span>Trundo</div>
  <h1 class="hero-title">LOREM IPSUM DOLOR SIT AMET</h1>
  <p class="hero-sub">Share cars in your city, save money and keep more vehicles off the street.</p>
  <form class="search">
    <div class="search-input">Type here</div>
    <div class="search-btn">Find Car</div>
  </form>
</section>

<section class="cars">
  <article class="car">
    <div class="car-photo" role="img" aria-label="Red hatchback car"><div class="price-tag">$40<small>DAY</small></div></div>
    <div class="owner"><div class="owner-photo" role="img" aria-label="Owner portrait"></div><div><div class="owner-name">Tobin Marsh (299)</div><div class="owner-note">Feedback in english only</div></div></div>
  </article>
  <article class="car">
    <div class="car-photo" role="img" aria-label="White sedan car"><div class="price-tag">$40<small>DAY</small></div></div>
    <div class="owner"><div class="owner-photo" role="img" aria-label="Owner portrait"></div><div><div class="owner-name">Tobin Marsh (299)</div><div class="owner-note">Feedback in english only</div></div></div>
  </article>
  <article class="car">
    <div class="car-photo" role="img" aria-label="Silver saloon car"><div class="price-tag">$40<small>DAY</small></div></div>
    <div class="owner"><div class="owner-photo" role="img" aria-label="Owner portrait"></div><div><div class="owner-name">Tobin Marsh (299)</div><div class="owner-note">Feedback in english only</div></div></div>
  </article>
</section>

<section class="band band-grey feature-one">
  <div class="inner" style="top:12px;height:120px">
    <div class="feature-text" style="width:340px">
      <h2 class="heading" style="font-size:15px">Laoreet dolore magna aliquamerat volutpat</h2>
      <p>Lorem ipsum dolor sit amet, consectetuer adipiscing elit, sed diam nonummy nibh euismod tincidunt ut laoreet dolore magna aliquam erat volutpat. Ut wisi enim ad minim veniam, quis nostrud exerci tation ullamcorper suscipit lobortis nisl ut aliquip ex ea commodo consequat.</p>
      <p>Duis autem vel eum iriure dolor in hendrerit in vulputate velit esse molestie consequat, vel illum dolore eu feugiat nulla facilisis at vero eros.</p>
      <span class="read-more">Read more »</span>
    </div>
    <div class="video" role="img" aria-label="Video still of a man driving a car">
      <div class="play"><svg width="12" height="12" viewBox="0 0 12 12"><path d="M3 1 L11 6 L3 11 Z" fill="#333"/></svg></div>
    </div>
  </div>
</section>

<section class="band feature-two">
  <div class="inner" style="top:0;height:150px">
    <div class="hand-car" role="img" aria-label="Open hand holding a small red toy car"></div>
    <div class="feature-text" style="position:absolute;left:190px;top:18px;width:351px">
      <h2 class="heading green" style="font-size:17px;line-height:1.2">Your car is full covered wih<br>insurances</h2>
      <p>Lorem ipsum dolor sit amet, consectetuer adipiscing elit, sed diam nonummy nibh euismod tincidunt ut laoreet dolore magna aliquam erat volutpat. Ut wisi enim ad minim veniam, quis nostrud exerci tation.</p>
      <p>Duis autem vel eum iriure dolor in hendrerit in vulputate velit esse molestie consequat.</p>
      <span class="read-more">Read more »</span>
    </div>
  </div>
</section>

<section class="band band-grey feature-three">
  <div class="inner" style="top:12px;height:120px">
    <div class="feature-text" style="width:340px">
      <h2 class="heading" style="font-size:15px">Consecte tuer adipis cing elit</h2>
      <p>Lorem ipsum dolor sit amet, consectetuer adipiscing elit, sed diam nonummy nibh euismod tincidunt ut laoreet dolore magna aliquam erat volutpat. Ut wisi enim ad minim veniam, quis nostrud exerci tation ullamcorper.</p>
      <p>Sed diam nonummy nibh euismod tincidunt ut laoreet dolore magna aliquam erat volutpat, ut wisi enim ad minim veniam quis nostrud.</p>
      <span class="read-more">Read more »</span>
    </div>
    <aside class="widget">
      <div class="widget-head"><span>Trundo</span><span>Linkhall</span></div>
      <div class="widget-body">
        <div>1,024 people like Trundo</div>
        <div class="fans">
          <div class="fan" role="img" aria-label="Member avatar"></div>
          <div class="fan" role="img" aria-label="Member avatar"></div>
          <div class="fan" role="img" aria-label="Member avatar"></div>
          <div class="fan" role="img" aria-label="Member avatar"></div>
          <div class="fan" role="img" aria-label="Member avatar"></div>
          <div class="fan" role="img" aria-label="Member avatar"></div>
        </div>
      </div>
      <span class="widget-btn">Like</span>
    </aside>
  </div>
</section>

<section class="press">
  <h2 class="heading green press-title">News paper logos</h2>
  <div class="press-row">
    <span class="arrow">‹</span>
    <span class="press-name">Northgate Times</span>
    <span class="press-name">The Westerly</span>
    <span class="press-name">Daily Harlow</span>
    <span class="press-name">Ember&amp;Slate</span>
    <span class="arrow">›</span>
  </div>
</section>

<footer class="footer">
  <div class="footer-heads"><span>Quick Links</span><span>Contact Us</span><span>Location Map</span><span>Follow Us</span></div>
  <div class="footer-cols">
    <ul class="fcol">
      <li>List Your Car</li><li>Sign up</li><li>Login</li><li>Registrance</li><li>Search</li><li>Search Particular Car</li>
    </ul>
    <div class="fcol">
      <div class="contact-line"><i></i>Street name 12 area,</div>
      <div style="padding-left:11px">Green district 4410</div>
      <div class="contact-line" style="margin-top:4px"><i></i>012 555 0148</div>
      <div class="contact-line" style="margin-top:4px"><i></i>info@trundo.com</div>
    </div>
    <div class="fcol"><div class="world" role="img" aria-label="World map showing service locations"></div></div>
    <div class="fcol">
      <div class="socials"><i></i><i></i><i></i><i></i><i></i><i></i></div>
      <div class="foot-brand"><span class="brand-dot"></span>Trundo</div>
      <div class="copy">Copyright ©2013. Trundo. All rights reserved</div>
    </div>
  </div>
</footer>

</body>
</html>
```